Corporate brochure design 4 pages

Hi,

We are a real estate company based in Europe.

We have almost finalized a rebranding.

We are developing a brand book guidelines (still on working process) to help you undertstand the look and feel of our new CI. I would like to receive proposals of design for a corporate brochure template. I need to receive the Indesign files with full ownership rights to be able to adapt all our documentation with this template.
Regarding the images, you can take gabaris on www.pelvaromedia.com. I will be able to take them afterwards.

There will be 4 pages. you will receive the 4 pages on pdf for your consideration with our (almost) actual layout.

- 1st page: cover
- 2nd page: company presentation in french and english
- 3rd page: some market data + graph
- 4th page: 2 retail centers presentation.

In the template, i need to have:
- the paragraph styles in order
- 2 different masters with top/bottom/page number aso.

Please feel free to ask any other questions.

best regards,
Updates

I would like to precise tha t we are active on the commercial real estate sector:

- office transactions (rent /sales)
- property management of administrative and business buildings
- Valuation of properties
- Capital markets (investment advices for selling building)

Industry/Entity Type

Real Estate

Colors

Designer to choose colors to be used in the design.

```html
<!DOCTYPE html>
<html lang="en">
<head>
<meta charset="utf-8">
<title>Ardenvale – Corporate Brochure</title>
<link href="https://fonts.googleapis.com/css2?family=Roboto:wght@300;400;700&display=swap" rel="stylesheet">
<style>
:root{
  --orange:#f26a21;
  --orange-soft:#fbd9c4;
  --ink:#1a1a1a;
  --text:#555;
  --grey:#d6d6d6;
  --grey-light:#efefef;
  --canvas:#e8e8e8;
  --white:#fff;
}
*{box-sizing:border-box;margin:0;padding:0}
html,body{width:1200px;height:425px;overflow:hidden}
body{background:var(--canvas);font-family:'Roboto',Arial,sans-serif;color:var(--text);position:relative}
.page{position:absolute;top:0;height:425px;background:var(--white);overflow:hidden}
.abs{position:absolute}
.footer-band{position:absolute;left:0;right:0;bottom:0;height:26px;background:var(--grey)}
.brand{position:absolute;bottom:6px;background:var(--white);padding:3px 6px 2px;text-align:right}
.brand-name{font-weight:700;font-size:15px;letter-spacing:.5px;color:var(--ink);line-height:1}
.brand-tag{font-size:5.2px;color:var(--orange);letter-spacing:.6px;line-height:1.4}
.folio{position:absolute;bottom:0;width:22px;height:32px;color:var(--white);font-size:9px;font-weight:300;display:flex;align-items:flex-end;justify-content:center;padding-bottom:8px}
.photo{position:absolute}
.body-copy{font-size:4.6px;line-height:1.5;color:var(--text)}
.kicker{font-size:6.5px;font-weight:700;color:var(--orange);text-transform:uppercase}
.kicker span{text-transform:none;font-weight:400;color:var(--ink)}
.page-title{font-weight:300;font-size:17px;color:var(--ink)}

/* cover */
.cover{left:0;width:296px}
.cover .title{position:absolute;left:18px;top:312px;font-size:26px;font-weight:300;color:var(--ink);line-height:1.1}
.cover .services{position:absolute;left:20px;top:344px;font-size:4.8px;line-height:1.4;color:var(--orange);list-style:none}
.cover .services b{font-weight:700}

/* company */
.company{left:301px;width:297px}
.company .top-rule{position:absolute;left:18px;right:0;top:0;height:4px;background:var(--orange)}
.company .margin-strip{position:absolute;left:0;top:0;bottom:0;width:14px;background:var(--grey-light)}
.company .page-title{position:absolute;left:18px;top:14px;color:var(--orange);font-size:17px}
.gallery-item{position:absolute;width:96px}
.gallery-item .photo{position:relative;height:66px}
.gallery-item .photo span{position:absolute;left:6px;top:24px;font-size:13px;font-weight:300;color:rgba(255,255,255,.8)}
.gallery-item p{font-size:4.2px;line-height:1.4;color:var(--orange);margin-top:3px}
.side-note{position:absolute;left:222px;top:285px;width:62px}
.side-note h4{font-size:6.5px;font-weight:400;color:var(--orange);margin-bottom:4px}

/* stock */
.stock{left:602px;width:296px}
.stock .header{position:absolute;left:0;right:0;top:0;height:38px;background:var(--grey)}
.stock .header h2{position:absolute;left:18px;top:14px;font-weight:300;font-size:17px;color:var(--white)}
.stock .header h2 small{font-size:4px}
.intro{position:absolute;top:45px;width:128px;font-size:4.6px;line-height:1.5;color:var(--ink)}
.intro .big{font-size:10px;font-weight:300}
.stock-table{position:absolute;left:0;top:97px;border-collapse:collapse;width:296px;table-layout:fixed}
.stock-table th{height:10px;font-size:4.8px;font-weight:700;color:var(--ink);text-align:left;padding:0;border-top:1px solid var(--orange-soft);border-bottom:1px solid var(--orange-soft)}
.stock-table td{height:8px;font-size:5.4px;color:var(--text);line-height:8px;padding:0;white-space:nowrap;overflow:hidden}
.stock-table .total td{height:10px;border-top:1px solid var(--orange-soft);border-bottom:1px solid var(--orange-soft)}
.stock-table .total .lbl{font-size:4.5px;text-align:right;padding-right:10px}
.stock-table .gap td{height:10px}
.zone{position:absolute;left:18px;font-size:15px;font-weight:300;color:var(--orange);line-height:1.05;white-space:nowrap}
.zone small{display:block;font-size:10px}
.grand-total{position:absolute;left:102px;top:313px;font-size:9px;font-weight:300;color:var(--ink)}
.grand-total span{position:absolute;left:96px;top:2px;font-size:6px;color:var(--text);white-space:nowrap}
.source{position:absolute;right:14px;top:325px;font-size:4px;color:var(--text)}
.chart{position:absolute;left:6px;top:328px}

/* retail */
.retail{left:902px;width:298px}
.retail .page-title{position:absolute;left:18px;top:18px;font-size:17px}
.centre{position:absolute;left:18px;width:272px}
.centre h3{font-size:6px;font-weight:700;color:var(--orange);padding-bottom:3px;border-bottom:1px solid var(--orange-soft)}
.facts{position:absolute;top:14px;left:0;width:166px;font-size:4.6px;line-height:1.5;color:var(--ink)}
.facts .row{display:flex}
.facts .row dt{width:80px;flex:none}
.facts .row dd{flex:1}
.facts .note{color:var(--orange);font-size:3.6px}
.map{position:absolute;right:0;background:radial-gradient(circle at 55% 45%,#c9c9c9,#e9e9e9 70%)}
</style>
</head>
<body>

<section class="page cover">
  <div class="photo" role="img" aria-label="Skyline of tall office towers against a blue sky" style="left:0;top:196px;width:296px;height:106px;background:linear-gradient(180deg,#2f5fa8 0%,#6f95c9 45%,#b9c7d6 100%)"></div>
  <h1 class="title">Corporate Brochure</h1>
  <ul class="services">
    <li><b>Something important you want to share/ emphasize upfront!</b></li>
    <li>Commercial real estate sector</li>
    <li>Office transactions (rent /sales)</li>
    <li>Property management of administrative and business buildings</li>
    <li>Valuation of properties</li>
    <li>Capital markets (investment advices for selling building)</li>
  </ul>
  <div class="footer-band"></div>
  <div class="brand" style="right:6px"><div class="brand-name">ARDENVALE</div><div class="brand-tag">COMMERCIAL REAL ESTATE</div></div>
</section>

<section class="page company">
  <div class="margin-strip"></div>
  <div class="top-rule"></div>
  <div class="photo" role="img" aria-label="Faded glass office facade" style="left:215px;top:14px;width:82px;height:180px;background:linear-gradient(90deg,#fff 0%,#e6e6e6 60%,#d2d2d2 100%)"></div>
  <h2 class="page-title">Company Presentation</h2>
  <div class="abs" style="left:20px;top:44px;width:195px">
    <p class="kicker">Lorem ipsum <span>(French)</span></p>
    <p class="body-copy" style="margin-top:3px">Dolor sit amet, consectetur adipiscing elit. Sed porttitor tellus velit, vel luctus nisl mattis eu. Ut et cursus libero, lobortis mattis leo. Donec nibh arcu, facilisis in porta a, condimentum ac magna. Donec euismod vulputate tincidunt.</p>
    <p class="body-copy" style="margin-top:4px">Etiam auctor, enim ut pulvinar luctus, libero massa tempor nisl, at porttitor dui tellus eget mauris. Class aptent taciti sociosqu ad litora torquent per conubia nostra, per inceptos himenaeos. Morbi eget condimentum lorem, vel pellentesque tortor. Curabitur egestas justo at mattis malesuada.</p>
    <p class="kicker" style="margin-top:8px">Lorem ipsum <span>(English)</span></p>
    <p class="body-copy" style="margin-top:3px">Dolor sit amet, consectetur adipiscing elit. Sed porttitor tellus velit, vel luctus nisl mattis eu. Ut et cursus libero, lobortis mattis leo. Donec nibh arcu, facilisis in porta a, condimentum ac magna. Donec euismod vulputate tincidunt.</p>
    <p class="body-copy" style="margin-top:4px">Etiam auctor, enim ut pulvinar luctus, libero massa tempor nisl, at porttitor dui tellus eget mauris. Class aptent taciti sociosqu ad litora torquent per conubia nostra, per inceptos himenaeos. Morbi eget condimentum lorem, vel pellentesque tortor. Curabitur egestas justo at mattis malesuada.</p>
  </div>
  <figure class="gallery-item" style="left:21px;top:196px">
    <div class="photo" role="img" aria-label="Glass tower facade seen from below" style="background:linear-gradient(160deg,#5d7fa6,#a9c0d8)"><span>Lorem ipsum</span></div>
    <p>Dolor sit amet, consectetur adipiscing elit. Sed porttitor tellus velit, vel luctus nisl mattis eu.</p>
  </figure>
  <figure class="gallery-item" style="left:124px;top:196px">
    <div class="photo" role="img" aria-label="Steel and glass atrium roof structure" style="background:linear-gradient(160deg,#8e9aa6,#d3dae0)"><span>Lorem ipsum</span></div>
    <p>Dolor sit amet, consectetur adipiscing elit. Sed porttitor tellus velit, vel luctus nisl mattis eu.</p>
  </figure>
  <figure class="gallery-item" style="left:21px;top:280px">
    <div class="photo" role="img" aria-label="Modern office interior with round atrium" style="background:linear-gradient(160deg,#7d8fa6,#c4cbd6)"><span>Lorem ipsum</span></div>
    <p>Dolor sit amet, consectetur adipiscing elit. Sed porttitor tellus velit, vel luctus nisl mattis eu.</p>
  </figure>
  <figure class="gallery-item" style="left:124px;top:280px">
    <div class="photo" role="img" aria-label="Furnished apartment floor plan in 3D" style="background:linear-gradient(160deg,#8a6f55,#d4c3ae)"><span>Lorem ipsum</span></div>
    <p>Dolor sit amet, consectetur adipiscing elit. Sed porttitor tellus velit, vel luctus nisl mattis eu.</p>
  </figure>
  <aside class="side-note">
    <h4>Side Note</h4>
    <p class="body-copy">Dolor sit amet, consectetur adipiscing elit. Sed porttitor tellus velit, vel luctus nisl mattis eu. Ut et cursus libero, lobortis mattis leo. Donec nibh arcu, facilisis in porta a, condimentum ac magna. Donec euismod vulputate tincidunt.</p>
  </aside>
  <div class="footer-band"></div>
  <div class="brand" style="right:30px"><div class="brand-name">ARDENVALE</div><div class="brand-tag">COMMERCIAL REAL ESTATE</div></div>
  <div class="folio" style="right:0;background:var(--ink)">02</div>
</section>

<section class="page stock">
  <div class="header"><h2>Stock/ Stock <small>(english mode)</small></h2></div>
  <div class="intro" style="left:8px">Le stock de mètres carrés disponibles de bureaux a augmenté de<br><span class="big">0,36 %</span> au troisième trimestre de cette année grâce à la livraison de près de <span class="big">12 300 m².</span><br>Le stock total atteint ainsi <span style="font-size:7px">3 465 600 m².</span></div>
  <div class="intro" style="left:150px">The stock of available office square meters has increased by<br><span class="big">0,36%</span> during the third quarter of this year with the delivery of<br><span class="big">12,300 m².</span><br>The total stock reaches <span style="font-size:7px">3,465,600 sm².</span></div>

  <table class="stock-table">
    <colgroup><col style="width:115px"><col style="width:83px"><col style="width:45px"><col></colgroup>
    <tr><th></th><th>QUARTIERS-DISTRICTS</th><th>STOCK M²</th><th>STOCK %</th></tr>
    <tr><td></td><td>Kirchberg</td><td>915 000</td><td>26,42 %</td></tr>
    <tr><td></td><td>CBD</td><td>806 400</td><td>23,27 %</td></tr>
    <tr><td></td><td>Station</td><td>382 700</td><td>11,04 %</td></tr>
    <tr><td></td><td>Cloche d'Or</td><td>365 600</td><td>10,55 %</td></tr>
    <tr><td></td><td>Limpertsberg</td><td>85 000</td><td>2,45 %</td></tr>
    <tr><td></td><td>Belair / Merl</td><td>67 800</td><td>1,96 %</td></tr>
    <tr><td></td><td>Hamm</td><td>44 500</td><td>1,28 %</td></tr>
    <tr><td></td><td>Kalchesbrück</td><td>33 000</td><td>0,95 %</td></tr>
    <tr class="total"><td></td><td class="lbl">Total</td><td>2 700 500</td><td>77,92 %</td></tr>
    <tr class="gap"><td colspan="4"></td></tr>
    <tr><td></td><td>Airport - Findel</td><td>157 500</td><td>4,54 %</td></tr>
    <tr><td></td><td>Bertrange / Bourmicht</td><td>82 000</td><td>2,37 %</td></tr>
    <tr><td></td><td>Strassen</td><td>81 050</td><td>2,34 %</td></tr>
    <tr><td></td><td>Howald</td><td>62 600</td><td>1,81 %</td></tr>
    <tr class="total"><td></td><td class="lbl">Total</td><td>383 150</td><td>11,06 %</td></tr>
    <tr class="gap"><td colspan="4"></td></tr>
    <tr><td></td><td>Belval</td><td>93 090</td><td>2,69 %</td></tr>
    <tr><td></td><td>Capellen</td><td>69 500</td><td>2,01 %</td></tr>
    <tr><td></td><td>Leudelange</td><td>73 556</td><td>2,12 %</td></tr>
    <tr><td></td><td>Munsbach</td><td>60 100</td><td>1,73 %</td></tr>
    <tr><td></td><td>Windhof</td><td>40 600</td><td>1,17 %</td></tr>
    <tr><td></td><td>Esch-sur-Alzette</td><td>24 700</td><td>0,71 %</td></tr>
    <tr><td></td><td>Contern</td><td>20 400</td><td>0,59 %</td></tr>
    <tr class="total"><td></td><td class="lbl">Total</td><td>381 946</td><td>11,02 %</td></tr>
  </table>
  <div class="zone" style="top:108px">Centre-ville<small>(City)</small></div>
  <div class="zone" style="top:190px">Ville-périphérie<small>(City-periphery)</small></div>
  <div class="zone" style="top:242px">Périphérie<small>(Periphery)</small></div>
  <div class="grand-total">Total<span>3 465 596</span></div>
  <div class="source">Source: Keystone Market Research</div>

  <svg class="chart" width="190" height="94" viewBox="0 0 190 94" aria-label="Office stock 2003 to 2013 bar chart">
    <g font-family="Roboto, Arial, sans-serif" font-size="4.2" fill="#555">
      <text x="0" y="8">3,600</text><text x="0" y="18">3,400</text><text x="0" y="28">3,200</text><text x="0" y="38">3,000</text><text x="0" y="48">2,800</text><text x="0" y="58">2,500</text><text x="0" y="68">2,000</text><text x="0" y="74">1,700</text>
    </g>
    <g fill="#cfcfcf">
      <rect x="16" y="52" width="11" height="22"/><rect x="29" y="48" width="11" height="26"/><rect x="42" y="44" width="11" height="30"/><rect x="55" y="40" width="11" height="34"/><rect x="68" y="35" width="11" height="39"/><rect x="81" y="27" width="11" height="47"/><rect x="94" y="21" width="11" height="53"/><rect x="107" y="18" width="11" height="56"/><rect x="120" y="16" width="11" height="58"/><rect x="133" y="12" width="11" height="62"/><rect x="146" y="10" width="11" height="64"/>
    </g>
    <g font-family="Roboto, Arial, sans-serif" font-size="3.6" fill="#555">
      <text x="17" y="80">2003</text><text x="30" y="80">2004</text><text x="43" y="80">2005</text><text x="56" y="80">2006</text><text x="69" y="80">2007</text><text x="82" y="80">2008</text><text x="95" y="80">2009</text><text x="108" y="80">2010</text><text x="121" y="80">2011</text><text x="134" y="80">2012</text><text x="148" y="80">YTD</text><text x="148" y="84">2013</text>
      <rect x="16" y="86" width="14" height="4" fill="#cfcfcf"/><text x="16" y="94">Stock</text>
    </g>
  </svg>

  <div class="photo" role="img" aria-label="Curved white building facade" style="right:0;bottom:0;width:22px;height:32px;background:linear-gradient(135deg,#9aa3ad,#dfe3e7)"></div>
  <div class="folio" style="right:0">03</div>
  <div class="brand" style="right:26px"><div class="brand-name">ARDENVALE</div><div class="brand-tag">COMMERCIAL REAL ESTATE</div></div>
</section>

<section class="page retail">
  <h2 class="page-title">Retail Centre</h2>

  <article class="centre" style="top:46px;height:140px">
    <h3>HIGH STREETS LUXEMBOURG: CITY - PEDESTRIAN ZONE</h3>
    <dl class="facts">
      <div class="row"><dt>Zone _Zone</dt><dd>Pedestrian zone: Rue des Tilleuls, Place Oriel …</dd></div>
      <div class="row"><dt>Stock _Stock</dt><dd>51 500 m² sm</dd></div>
      <div class="row"><dt>Magasins _Shops</dt><dd>+/- 400</dd></div>
      <div class="row"><dt>Niveau loyers _Rental bands<br><span class="note">(Loyers bruts par m²/month)</span></dt><dd>980 – 1 500</dd></div>
      <div class="row" style="margin-top:3px"><dt>Parking</dt><dd>3 900 (public)</dd></div>
      <div class="row"><dt>Marques principales _Main brands</dt><dd>3 600 (public): Maison Orvessa, Quenvale, Castelune, Velnora, Tessaro &amp; Lys, Beauté Ilvane, Marvello Dusen, Arbosé, Quintale, Torrelle, Ombrine, Zelvano, Duvessa, Orlanthe, Pellisca, Vantrelle, Sorvane, Ilmara, Brevonne…</dd></div>
    </dl>
    <div class="photo" role="img" aria-label="Busy pedestrian shopping street" style="left:0;top:96px;width:64px;height:42px;background:linear-gradient(160deg,#8d7b63,#c9b89c)"></div>
    <div class="map" role="img" aria-label="City map locating the pedestrian zone" style="top:10px;width:100px;height:100px"></div>
  </article>

  <article class="centre" style="top:196px;height:140px">
    <h3>HIGH STREETS LUXEMBOURG STATION AV. GARE</h3>
    <dl class="facts">
      <div class="row"><dt>Zone _Zone</dt><dd>Avenue Belmont</dd></div>
      <div class="row"><dt>Stock _Stock</dt><dd>37 500 m² - sqm</dd></div>
      <div class="row"><dt>Magasins _Shops</dt><dd>+/- 120</dd></div>
      <div class="row"><dt>Niveau loyers _Rental bands<br><span class="note">(Loyers bruts par m²/month)</span></dt><dd>300 – 720 euros/sqm/year</dd></div>
      <div class="row" style="margin-top:3px"><dt>Parking</dt><dd>1 600 (public)</dd></div>
      <div class="row"><dt>Marques principales _Main brands</dt><dd>Kestrova, Lumarel, Talvesse, Orvanti, Nivelline, Quorabel, Sellavie, Drumoran, Vespelle, Halvéro, Ostrivane, Merilda, Tavolène, Corvanne, Pelmira, Ruvenne, Quillora, Orsenta, Marvolie…</dd></div>
    </dl>
    <div class="photo" role="img" aria-label="Avenue with shops and passers-by" style="left:0;top:100px;width:64px;height:40px;background:linear-gradient(160deg,#7e7a72,#c2bdb2)"></div>
    <div class="map" role="img" aria-label="City map locating the station avenue" style="top:10px;width:100px;height:96px"></div>
  </article>

  <div class="photo" role="img" aria-label="Curved white building facade" style="left:0;bottom:0;width:58px;height:32px;background:linear-gradient(135deg,#dfe3e7,#9aa3ad)"></div>
  <div class="brand" style="right:30px"><div class="brand-name">ARDENVALE</div><div class="brand-tag">COMMERCIAL REAL ESTATE</div></div>
  <div class="folio" style="right:0;height:40px;background:var(--orange)">04</div>
</section>

</body>
</html>
```